Varrow Business Card Design - Professional Flexible and forward thinking. Clean and Easy to follow

Management Consulting Company. I focus on business development and concept and operational review. I need a progressive, simple and professional layout design for the business cards, letterhead and envelops
Professional Flexible and forward thinking. Clean and Easy to follow
Mature Business persons and professionals and Corporations

Target Market(s)

Mature Business persons and professionals and Corporations - Government org.

Industry/Entity Type

Consulting

Contact Information for Business Card

Requirements
Must have
• Marcus Varrow
• President
• Phone - 347.682.1530
• email - Mvarrow@varrowpartners-example.com
• Skype - Marc.varrow
• 2187 Tollbrook Lane
• Suite A
• Massapequa, N.Y. 11492
• USA
Nice to have
• www.varrowpartners-example.com
Should not have
• N/A

```html
<!DOCTYPE html>
<html lang="en">
<head>
<meta charset="utf-8">
<title>Varrow Business Card Design</title>
<link href="https://fonts.googleapis.com/css2?family=Open+Sans:wght@400;600;700&display=swap" rel="stylesheet">
<style>
  :root {
    --brand-blue: #0a7fd0;
    --brand-white: #ffffff;
    --page-bg: #eceef1;
    --card-shadow: rgba(0, 0, 0, 0.14);
    --divider: rgba(255, 255, 255, 0.28);
    --watermark: #e8e8e8;
  }
  html, body {
    margin: 0;
    padding: 0;
    width: 1200px;
    height: 900px;
    overflow: hidden;
    background: var(--page-bg);
    font-family: "Open Sans", Arial, sans-serif;
  }
  .canvas {
    position: relative;
    width: 1200px;
    height: 900px;
  }
  .card {
    position: absolute;
    background: var(--brand-white);
    box-shadow: 0 6px 20px var(--card-shadow);
    overflow: hidden;
  }

  /* Front card */
  .card-front {
    left: 77px;
    top: 34px;
    width: 589px;
    height: 364px;
  }
  .card-front .brand {
    position: absolute;
    left: 31px;
    top: 0;
    height: 156px;
    display: flex;
    align-items: center;
    gap: 22px;
  }
  .brand-mark {
    width: 88px;
    height: 88px;
    border-radius: 50%;
    border: 7px solid var(--brand-blue);
    box-sizing: border-box;
  }
  .brand-name {
    font-weight: 600;
    font-size: 38px;
    letter-spacing: 0.5px;
    color: var(--brand-blue);
    white-space: nowrap;
  }
  .card-front .info-panel {
    position: absolute;
    left: 0;
    top: 156px;
    width: 100%;
    height: 208px;
    background: var(--brand-blue);
    color: var(--brand-white);
  }
  .person-name {
    position: absolute;
    left: 31px;
    top: 34px;
    margin: 0;
    font-size: 19px;
    font-weight: 700;
    line-height: 1.2;
  }
  .person-title {
    position: absolute;
    left: 31px;
    top: 60px;
    margin: 0;
    font-size: 15px;
    font-weight: 400;
    line-height: 1.2;
  }
  .contact-list {
    position: absolute;
    top: 99px;
    margin: 0;
    padding: 0;
    list-style: none;
  }
  .contact-list-primary {
    left: 0;
    width: 330px;
  }
  .contact-list-secondary {
    left: 340px;
    width: 249px;
  }
  .contact-item {
    display: flex;
    align-items: center;
    gap: 10px;
    height: 31px;
    font-size: 14px;
    white-space: nowrap;
    border-bottom: 1px solid var(--divider);
  }
  .contact-list-primary .contact-item { padding-left: 33px; }
  .contact-list-secondary .contact-item { padding-left: 0; }
  .contact-item:last-child { border-bottom: none; }
  .contact-item.is-continued { padding-left: 23px; }
  .contact-icon { width: 13px; height: 13px; flex: none; }

  /* Back card */
  .card-back {
    left: 388px;
    top: 505px;
    width: 567px;
    height: 352px;
  }
  .card-back .brand-band {
    position: absolute;
    left: 0;
    top: 36px;
    width: 100%;
    height: 130px;
    background: var(--brand-blue);
    display: flex;
    align-items: center;
    justify-content: center;
    gap: 20px;
  }
  .card-back .brand-mark {
    width: 80px;
    height: 80px;
    border-color: var(--brand-white);
    border-width: 6px;
  }
  .card-back .brand-name {
    color: var(--brand-white);
    font-size: 33px;
  }
  .card-back .watermark {
    position: absolute;
    left: -30px;
    top: 170px;
    width: 330px;
    height: 330px;
    border-radius: 50%;
    border: 16px solid var(--watermark);
    box-sizing: border-box;
  }
</style>
</head>
<body>
<main class="canvas">
  <section class="card card-front" aria-label="Business card front">
    <div class="brand">
      <span class="brand-mark" aria-hidden="true"></span>
      <span class="brand-name">Varrow Associates</span>
    </div>
    <div class="info-panel">
      <h1 class="person-name">Marcus Varrow</h1>
      <p class="person-title">President</p>
      <ul class="contact-list contact-list-primary">
        <li class="contact-item">
          <svg class="contact-icon" viewBox="0 0 24 24" aria-hidden="true"><path fill="#fff" d="M6.6 10.8a15.1 15.1 0 0 0 6.6 6.6l2.2-2.2c.3-.3.7-.4 1-.2 1.1.4 2.3.6 3.6.6.6 0 1 .4 1 1V20c0 .6-.4 1-1 1A17 17 0 0 1 3 4c0-.6.4-1 1-1h3.5c.6 0 1 .4 1 1 0 1.3.2 2.5.6 3.6.1.3 0 .7-.2 1z"/></svg>
          <span>347.682.1530</span>
        </li>
        <li class="contact-item">
          <svg class="contact-icon" viewBox="0 0 24 24" aria-hidden="true"><path fill="#fff" d="M2 5h20v14H2z"/><path fill="none" stroke="#0a7fd0" stroke-width="2" d="M2.5 5.5 12 13l9.5-7.5"/></svg>
          <span>Mvarrow@varrowpartners-example.com</span>
        </li>
        <li class="contact-item">
          <svg class="contact-icon" viewBox="0 0 24 24" aria-hidden="true"><g fill="none" stroke="#fff" stroke-width="2.6" stroke-linecap="round"><path d="M10 14a4.5 4.5 0 0 0 6.4 0l3.3-3.3a4.5 4.5 0 0 0-6.4-6.4l-1.2 1.2"/><path d="M14 10a4.5 4.5 0 0 0-6.4 0l-3.3 3.3a4.5 4.5 0 0 0 6.4 6.4l1.2-1.2"/></g></svg>
          <span>www.varrowpartners-example.com</span>
        </li>
      </ul>
      <ul class="contact-list contact-list-secondary">
        <li class="contact-item">
          <svg class="contact-icon" viewBox="0 0 24 24" aria-hidden="true"><circle cx="12" cy="12" r="9" fill="none" stroke="#fff" stroke-width="2.6"/><path fill="none" stroke="#fff" stroke-width="2.4" stroke-linecap="round" d="M15 9c-1-1.2-4.5-1.4-5 .5-.6 2.3 5.6 1.4 5 4.2-.5 1.9-4.2 1.8-5.3.3"/></svg>
          <span>Marc.varrow</span>
        </li>
        <li class="contact-item">
          <svg class="contact-icon" viewBox="0 0 24 24" aria-hidden="true"><path fill="#fff" d="M12 2a7 7 0 0 0-7 7c0 5.2 7 13 7 13s7-7.8 7-13a7 7 0 0 0-7-7zm0 9.5A2.5 2.5 0 1 1 12 6.5a2.5 2.5 0 0 1 0 5z"/></svg>
          <span>2187 Tollbrook Lane, Suite A</span>
        </li>
        <li class="contact-item is-continued">
          <span>Massapequa, N.Y. 11492, USA</span>
        </li>
      </ul>
    </div>
  </section>

  <section class="card card-back" aria-label="Business card back">
    <div class="brand-band">
      <span class="brand-mark" aria-hidden="true"></span>
      <span class="brand-name">Varrow Associates</span>
    </div>
    <span class="watermark" aria-hidden="true"></span>
  </section>
</main>
</body>
</html>
```